"Brindle Oak Accupuncture" needs a Promotional Card - A6 size

Requirements
Must have
• Bright colours, pictures of happy people, acupuncture-related pictures.

```html
<!DOCTYPE html>
<html lang="en">
<head>
<meta charset="utf-8">
<title>Brindle Oak Accupuncture – Promotional Card</title>
<link rel="stylesheet" href="https://fonts.googleapis.com/css2?family=PT+Sans:wght@400;700&family=PT+Sans+Narrow:wght@400;700&display=swap">
<style>
  :root {
    --stage: #ece9e3;
    --green-dark: #6fa33c;
    --green: #8cc04f;
    --green-light: #b5d872;
    --brown: #4a3328;
    --brown-line: #7a5a44;
    --red: #e3261d;
    --white: #ffffff;
    --ink: #2f2a26;
    --paper: #f3f3ef;
  }
  * { box-sizing: border-box; margin: 0; padding: 0; }
  html, body { width: 1200px; height: 508px; overflow: hidden; background: var(--stage); }
  .canvas { position: relative; width: 1200px; height: 508px; overflow: hidden; background: var(--stage); font-family: "PT Sans", sans-serif; }

  .card { position: absolute; top: 57px; height: 393px; overflow: hidden; box-shadow: 0 2px 6px rgba(0,0,0,.25); }
  .card--front { left: 35px; width: 555px; background: linear-gradient(160deg, var(--green-dark) 0%, var(--green) 55%, var(--green-light) 100%); }
  .card--back { left: 621px; width: 542px; background: linear-gradient(170deg, var(--paper) 0%, #eef2e4 45%, #c9e09a 100%); }

  .layer { position: absolute; inset: 0; }

  .front-headline { position: absolute; top: 10px; left: 0; width: 100%; text-align: center; color: var(--white); font-family: "PT Sans", sans-serif; font-weight: 700; font-size: 22px; line-height: 30px; }

  .brand-seal { position: absolute; border-radius: 50%; background: var(--brown); display: flex; align-items: center; justify-content: center; text-align: center; color: #f2b84b; font-family: "PT Sans", sans-serif; font-weight: 700; line-height: 1.15; }
  .card--front .brand-seal { left: 232px; top: 156px; width: 92px; height: 92px; font-size: 13px; }
  .card--back .brand-seal { left: 44px; top: 48px; width: 82px; height: 82px; font-size: 11.5px; }

  .relief-list { position: absolute; top: 279px; left: 0; width: 100%; text-align: center; color: var(--white); font-family: "PT Sans Narrow", sans-serif; font-weight: 700; font-size: 15px; line-height: 22px; font-variant: small-caps; }

  .footer-band { position: absolute; left: 0; bottom: 0; width: 100%; border-top: 3px solid var(--brown-line); }
  .card--front .footer-band { height: 73px; background: linear-gradient(90deg, #7cb144 0%, #9fcd63 60%, #b3d97a 100%); }
  .card--back .footer-band { height: 60px; background: linear-gradient(90deg, #79ad43 0%, #97c65b 60%, #a9d06d 100%); border-top: none; }

  .clinic-address { position: absolute; color: var(--white); font-family: "PT Sans Narrow", sans-serif; font-weight: 700; font-size: 15px; line-height: 18px; }
  .card--front .clinic-address { left: 59px; top: 10px; }
  .card--back .clinic-address { left: 65px; top: 6px; }

  .booking { position: absolute; text-align: left; }
  .card--front .booking { left: 264px; top: 6px; }
  .card--back .booking { left: 286px; top: 5px; text-align: center; }
  .booking__lead { font-family: "PT Sans Narrow", sans-serif; font-weight: 700; font-size: 17px; line-height: 20px; }
  .card--front .booking__lead { color: var(--brown); }
  .card--back .booking__lead { color: var(--white); }
  .booking__phone { display: flex; align-items: center; gap: 8px; font-family: "PT Sans Narrow", sans-serif; font-weight: 700; font-size: 31px; line-height: 36px; letter-spacing: .5px; }
  .card--front .booking__phone { color: var(--red); margin-left: 14px; }
  .card--back .booking__phone { color: var(--white); }
  .phone-icon { width: 22px; height: 22px; flex: none; }

  .back-headline { position: absolute; left: 192px; top: 15px; width: 340px; color: var(--brown); font-family: "PT Sans Narrow", sans-serif; font-weight: 700; font-size: 26px; line-height: 27px; }
  .back-headline__call { display: block; color: var(--red); font-size: 30px; line-height: 32px; }
  .back-intro { position: absolute; left: 192px; top: 112px; width: 270px; color: var(--ink); font-family: "PT Sans Narrow", sans-serif; font-size: 16px; line-height: 18px; }

  .about { position: absolute; left: 357px; top: 158px; width: 175px; color: var(--ink); }
  .about__title { font-family: "PT Sans Narrow", sans-serif; font-weight: 700; font-size: 17px; line-height: 20px; margin-bottom: 5px; }
  .about__name { font-family: "PT Sans Narrow", sans-serif; font-size: 11px; line-height: 14px; }
  .about__name b { font-weight: 700; }
  .about__bio { font-family: "PT Sans Narrow", sans-serif; font-size: 11px; line-height: 13px; }
</style>
</head>
<body>
<main class="canvas">

  <!-- Front of card -->
  <section class="card card--front">
    <svg class="layer" width="555" height="393" viewBox="0 0 555 393">
      <g role="img" aria-label="Photo of a relaxed woman lying down with acupuncture needles in her shoulder">
        <path d="M0,82 Q140,66 258,62 L258,150 Q200,212 110,222 Q50,228 0,214 Z" fill="url(#photoLeft)"/>
      </g>
      <g role="img" aria-label="Photo of a smiling woman receiving facial acupuncture">
        <path d="M298,62 Q430,64 555,82 L555,222 Q500,232 440,222 Q350,208 298,150 Z" fill="url(#photoRight)"/>
      </g>
      <path d="M0,82 Q140,66 258,62 M298,62 Q430,64 555,82" fill="none" stroke="var(--brown-line)" stroke-width="3"/>
      <path d="M0,214 Q50,228 110,222 Q200,212 258,150 M298,150 Q350,208 440,222 Q500,232 555,222" fill="none" stroke="var(--brown-line)" stroke-width="3"/>
      <path d="M258,60 L298,60 L298,150 Q300,170 278,190 Q256,170 258,150 Z" fill="#7cb244"/>
      <defs>
        <linearGradient id="photoLeft" x1="0" y1="0" x2="1" y2="1">
          <stop offset="0" stop-color="#f1e4dc"/>
          <stop offset=".55" stop-color="#e6c3ad"/>
          <stop offset="1" stop-color="#f6f1ee"/>
        </linearGradient>
        <linearGradient id="photoRight" x1="0" y1="0" x2="1" y2="1">
          <stop offset="0" stop-color="#f3ece6"/>
          <stop offset=".5" stop-color="#e8c8b4"/>
          <stop offset="1" stop-color="#d9c2a4"/>
        </linearGradient>
      </defs>
    </svg>

    <h1 class="front-headline">Acupuncture can rebalance your body, clear your<br>mind&nbsp; and improve your health and well-being</h1>

    <div class="brand-seal">Brindle Oak<br>Accupuncture</div>

    <p class="relief-list">Relief for: Back pain and Neck pain • Headache/Migraines • Stress and Anxiety • Weight Loss<br>• Insomnia • Sciatica • Infertility • PMS/Menopause • Arthritis • Sprains and more</p>

    <footer class="footer-band">
      <address class="clinic-address" style="font-style:normal">Brindle Oak Accupuncture Clinic<br>42 Rowan Lane<br>London, NW4 2QP</address>
      <div class="booking">
        <p class="booking__lead">Call us today to book your appointment</p>
        <p class="booking__phone">
          <svg class="phone-icon" viewBox="0 0 24 24"><circle cx="12" cy="12" r="11" fill="none" stroke="currentColor" stroke-width="1.6"/><path d="M9 6.5c-1.2.6-1.8 2-1.3 4.2.6 2.6 2.4 5.4 4.6 6.8 1.4.9 2.5.8 3.2.3l-1.6-2.4c-.4.2-.9.2-1.4-.2-1-.9-2-2.6-2.3-3.9-.1-.6.1-1 .4-1.2z" fill="currentColor"/></svg>
          020.555.0148
        </p>
      </div>
    </footer>
  </section>

  <!-- Back of card -->
  <section class="card card--back">
    <svg class="layer" width="542" height="393" viewBox="0 0 542 393">
      <defs>
        <linearGradient id="bamboo" x1="0" y1="0" x2="1" y2="0">
          <stop offset="0" stop-color="#5e9a2c"/>
          <stop offset=".45" stop-color="#8fc451"/>
          <stop offset="1" stop-color="#bfe08a" stop-opacity="0"/>
        </linearGradient>
        <linearGradient id="cupping" x1="0" y1="0" x2="1" y2="1">
          <stop offset="0" stop-color="#e9cdb9"/>
          <stop offset="1" stop-color="#b98a6c"/>
        </linearGradient>
        <linearGradient id="needles" x1="0" y1="0" x2="1" y2="1">
          <stop offset="0" stop-color="#d8b7a0"/>
          <stop offset="1" stop-color="#3a3431"/>
        </linearGradient>
        <linearGradient id="portrait" x1="0" y1="0" x2="0" y2="1">
          <stop offset="0" stop-color="#cbb3a3"/>
          <stop offset="1" stop-color="#6d4d45"/>
        </linearGradient>
      </defs>
      <g role="img" aria-label="Green bamboo stalks and leaves">
        <rect x="0" y="0" width="260" height="333" fill="url(#bamboo)"/>
      </g>
      <g role="img" aria-label="Photo of a woman receiving cupping therapy on her back">
        <rect x="20" y="122" width="126" height="82" fill="url(#cupping)" stroke="#8d8d86" stroke-width="3"/>
      </g>
      <g role="img" aria-label="Photo of hands placing acupuncture needles">
        <rect x="20" y="212" width="126" height="82" fill="url(#needles)" stroke="#8d8d86" stroke-width="3"/>
      </g>
      <g role="img" aria-label="Portrait photo of the acupuncturist">
        <circle cx="289" cy="208" r="50" fill="url(#portrait)" stroke="var(--white)" stroke-width="4"/>
      </g>
      <g aria-label="Professional membership badge">
        <rect x="214" y="275" width="127" height="44" fill="var(--white)"/>
        <rect x="222" y="286" width="62" height="6" fill="#c7d3e6"/>
        <rect x="222" y="297" width="48" height="4" fill="#dde5f0"/>
        <line x1="291" y1="282" x2="291" y2="312" stroke="#b8c4d6" stroke-width="1"/>
        <circle cx="316" cy="297" r="15" fill="#1e9fc0"/>
      </g>
    </svg>

    <div class="brand-seal">Brindle Oak<br>Accupuncture</div>

    <h2 class="back-headline">For Thousand of Years, Acupuncture<br>Has Helped Millions of People.<span class="back-headline__call">Now it’s YOUR turn</span></h2>

    <p class="back-intro">Acupuncture is safe, natural and effective solution for a variety of health condition.</p>

    <article class="about">
      <h3 class="about__title">About the Acupuncturist</h3>
      <p class="about__name"><b>MARA LIND</b>, Acupuncturist</p>
      <p class="about__bio">Lorem ipsum dolor sit amet, mel wisi similique in. Te ius solet ration ibus omittantur, ad utroque nomin avi invidunt ius, zril solet mollis in nam. Eu mazim suavitate pro. Ius quis appareat ne, eleifend reprimi que at mel, duo cu vide sensibus consulatu. At qui paulo admodum delectus, est at legimus philosophia, ex justo malorum sed.</p>
    </article>

    <footer class="footer-band">
      <address class="clinic-address" style="font-style:normal">Brindle Oak Accupuncture Clinic<br>42 Rowan Lane<br>London, NW4 2QP</address>
      <div class="booking">
        <p class="booking__lead">Call us today</p>
        <p class="booking__phone">
          <svg class="phone-icon" viewBox="0 0 24 24"><circle cx="12" cy="12" r="11" fill="none" stroke="currentColor" stroke-width="1.6"/><path d="M9 6.5c-1.2.6-1.8 2-1.3 4.2.6 2.6 2.4 5.4 4.6 6.8 1.4.9 2.5.8 3.2.3l-1.6-2.4c-.4.2-.9.2-1.4-.2-1-.9-2-2.6-2.3-3.9-.1-.6.1-1 .4-1.2z" fill="currentColor"/></svg>
          020.555.0148
        </p>
      </div>
    </footer>
  </section>

</main>
</body>
</html>
```